Paper Tides - post rock band album cover design

We are Paper Tides, a post-rock band based on San Jose, CA, USA. We will release a new album “Where the rivers fold" and need a album cover.

The new album is full of emotion and energy. song list:
1. Forward
2. Search (in uploaded files)
3. Before
4. Memory
5. Dream
6. Spring
7. Om Namah Shivaya

Please hear our previous music here
https://paper-tides.soundvault-example.com/album/paper-tides

Target Market(s)

music lovers

Industry/Entity Type

Music Download

Colors

Designer to choose colors to be used in the design.

Requirements
Must have
• album cover + back
• For cover we only need band name (do not need album name), want to use some streamline font for the band name "Paper Tides"
• I attached an example from another band
Nice to have
• I don't want to limit the designers, so please listen to the music and design what you feel the best:)

```html
<!DOCTYPE html>
<html lang="en">
<head>
<meta charset="utf-8">
<title>Paper Tides — Album Cover and Back</title>
<link href="https://fonts.googleapis.com/css2?family=Nunito+Sans:wght@300&display=swap" rel="stylesheet">
<style>
  :root {
    --page-black: #000000;
    --sky-deep: #141c1e;
    --aurora-green: #3f6a58;
    --aurora-teal: #2c4d4a;
    --aurora-violet: #4a3652;
    --horizon-pink: #d4446e;
    --horizon-rose: #8a3a5a;
    --ground-dark: #0a0a0c;
    --ink-light: #eef0ee;
    --rule-light: rgba(238, 240, 238, 0.85);
  }

  * { margin: 0; padding: 0; box-sizing: border-box; }

  html, body {
    width: 1200px;
    height: 601px;
    overflow: hidden;
    background: var(--page-black);
  }

  .spread {
    position: relative;
    width: 1200px;
    height: 601px;
    background: var(--page-black);
    font-family: "Nunito Sans", "Helvetica Neue", Arial, sans-serif;
    color: var(--ink-light);
  }

  .panel {
    position: absolute;
    top: 17px;
    height: 519px;
    overflow: hidden;
  }

  .panel--front { left: 26px; width: 555px; }
  .panel--back  { left: 608px; width: 567px; }

  .aurora-photo {
    position: absolute;
    inset: 0;
    background:
      linear-gradient(to top, var(--ground-dark) 0%, var(--ground-dark) 9%, rgba(10,10,12,0) 22%),
      radial-gradient(ellipse 55% 30% at 8% 78%, var(--horizon-pink) 0%, rgba(212,68,110,0.55) 45%, rgba(212,68,110,0) 100%),
      radial-gradient(ellipse 60% 35% at 25% 62%, rgba(138,58,90,0.75) 0%, rgba(138,58,90,0) 100%),
      radial-gradient(ellipse 45% 40% at 15% 35%, rgba(74,54,82,0.8) 0%, rgba(74,54,82,0) 100%),
      radial-gradient(ellipse 70% 55% at 70% 30%, rgba(63,106,88,0.85) 0%, rgba(63,106,88,0) 100%),
      radial-gradient(ellipse 50% 50% at 35% 10%, rgba(44,77,74,0.9) 0%, rgba(44,77,74,0) 100%),
      var(--sky-deep);
  }

  .panel--back .aurora-photo { filter: blur(2px) brightness(0.9); }

  .band-name {
    position: absolute;
    font-weight: 300;
    color: var(--ink-light);
    white-space: nowrap;
    letter-spacing: 0.02em;
  }

  .panel--front .band-name {
    left: 338px;
    top: 470px;
    font-size: 34px;
  }

  .panel--back .band-name {
    left: 0;
    width: 100%;
    top: 92px;
    text-align: center;
    font-size: 44px;
  }

  .rule {
    position: absolute;
    left: 173px;
    width: 222px;
    height: 1px;
    background: var(--rule-light);
  }

  .rule--top { top: 179px; }
  .rule--bottom { top: 493px; }

  .tracklist {
    position: absolute;
    left: 0;
    width: 100%;
    top: 206px;
    list-style: none;
    text-align: center;
    font-size: 22px;
    font-weight: 300;
    letter-spacing: 0.04em;
    line-height: 39.5px;
  }
</style>
</head>
<body>
  <main class="spread">
    <section class="panel panel--front" aria-label="Album front cover">
      <div class="aurora-photo" role="img" aria-label="Night sky with green and violet aurora over a pink horizon, a lone figure standing in silhouette on dark ground"></div>
      <h1 class="band-name">Paper Tides</h1>
    </section>

    <section class="panel panel--back" aria-label="Album back cover">
      <div class="aurora-photo" role="img" aria-label="Softly blurred aurora sky over a pink horizon with a silhouetted figure"></div>
      <h2 class="band-name">Paper Tides</h2>
      <div class="rule rule--top"></div>
      <ol class="tracklist">
        <li>01. Forward</li>
        <li>02. Search</li>
        <li>03. Before</li>
        <li>04. Memory</li>
        <li>05. Dream</li>
        <li>06. Spring</li>
        <li>07.&nbsp; Om Namah Shivaya</li>
      </ol>
      <div class="rule rule--bottom"></div>
    </section>
  </main>
</body>
</html>
```